Book & e-book cover - front, back and sleeve

Please see plot description:

The Lantern

A man lies dying and trapped in a parking garage stairwell. The poorly lit stairwell serves as a painful reminder of one of his memories of childhood locked in that darkened closet. To keep himself in tact he would play with a shiny silver button he ripped off from his pajamas – throwing it in the air and tapping the floor to find it. As he lies trapped and dying that same defeated and abandoned feeling descends upon him. As he comes in and out of consciousness memories from his past manifest themselves and we are introduced to the turbulent and sometimes triumphant pathway that has led him to his current state. It is up to him to sort through the barrage of emotions to find his way out, to let go, to forgive. That is if his heart will let him.
Updates

I know that we mentioned having a photograph of a button on the cover but we would like to see examples of covers with a more abstract or drawn or painted looking button.  Thanks.

Target Market(s)

Dramatic story - geared towards adult readers

Industry/Entity Type

Parking

Requirements
Must have
• Simple, crisp, custom, classic look. Do not want it to look to sci-fi or medival - this is an emotional story - a memoir.

Items on the front cover:

Title: The Lantern
Author: R.L. Marsh
Words: A Novel
Photo: a sliver button (just one image)

Items on the back cover

Plot description area
ISBN area at bottom

Nice to have
• Please see examples that have been uploaded. I like novels with a textured background.

A simple button on the cover with the right fonts and colour scheme.
Should not have
• I do not want a person or icons used on the cover
I do not want it to busy.
Do not want it to feel like it is a sci-fi novel or medival story.
Do not want the cover to be too "dark" - I do not want potential readers to get the wrong idea of what "The Lantern" is about.

```html
<!DOCTYPE html>
<html lang="en">
<head>
<meta charset="utf-8">
<title>The Lantern — book cover</title>
<link rel="stylesheet" href="https://fonts.googleapis.com/css2?family=Poiret+One&display=swap">
<style>
  :root {
    --paper: #e4e4e2;
    --stone: #c9c9c6;
    --stone-dark: #a9a8a4;
    --haze: rgba(245,245,243,0.55);
    --ink: #1a1a1a;
    --ink-soft: #2e2e2e;
    --white: #ffffff;
    --amber: rgba(176,140,70,0.55);
    --button-light: rgba(250,250,248,0.95);
    --button-mid: rgba(215,215,212,0.85);
    --button-edge: rgba(160,160,156,0.6);
    --isbn-box: rgba(255,255,255,0.7);
    --isbn-line: rgba(60,60,60,0.35);
  }
  * { margin: 0; padding: 0; box-sizing: border-box; }
  html, body { width: 1200px; height: 818px; overflow: hidden; background: var(--paper); }
  .cover {
    position: relative;
    width: 1200px;
    height: 818px;
    overflow: hidden;
    font-family: "Poiret One", sans-serif;
    color: var(--ink);
  }
  .cover-photo {
    position: absolute; inset: 0;
    background:
      linear-gradient(180deg, transparent 47%, var(--amber) 48.5%, transparent 50%),
      radial-gradient(ellipse at 78% 25%, #d4d4d1 0%, transparent 60%),
      linear-gradient(90deg, var(--stone) 0%, var(--stone-dark) 45%, var(--stone) 60%, #d8d8d5 100%),
      linear-gradient(180deg, var(--stone) 0%, #e9e9e7 100%);
  }
  .back-haze {
    position: absolute; left: 0; top: 0; bottom: 0; width: 560px;
    background: linear-gradient(90deg, var(--haze) 0%, var(--haze) 80%, transparent 100%);
  }
  .button-photo {
    position: absolute;
    border-radius: 50%;
    background: radial-gradient(circle at 45% 40%, var(--button-light) 0%, var(--button-mid) 60%, var(--button-edge) 100%);
    box-shadow: 0 0 18px rgba(255,255,255,0.6);
  }
  .button-front { left: 691px; top: 381px; width: 128px; height: 128px; }
  .button-back { left: 68px; top: 677px; width: 118px; height: 64px; }
  .blurb {
    position: absolute; left: 50px; top: 22px; width: 410px;
    font-size: 17.5px; line-height: 21.4px; color: var(--ink-soft);
  }
  .blurb-label { font-size: 14px; margin-bottom: 7px; }
  .blurb p { margin-bottom: 7px; }
  .isbn-area {
    position: absolute; left: 400px; top: 712px; width: 130px; height: 74px;
    background: var(--isbn-box);
    border: 1px solid var(--isbn-line);
  }
  .spine-author, .spine-title {
    position: absolute;
    writing-mode: vertical-rl;
    line-height: 1;
    white-space: nowrap;
  }
  .spine-author { left: 584px; top: 82px; font-size: 40px; color: var(--white); }
  .spine-title { left: 570px; top: 432px; font-size: 72px; color: var(--ink); }
  .front-author {
    position: absolute; left: 936px; top: 606px;
    font-size: 41px; color: var(--white); line-height: 1; white-space: nowrap;
  }
  .front-title {
    position: absolute; left: 798px; top: 638px;
    font-size: 70px; font-weight: 400; color: var(--ink); line-height: 1; white-space: nowrap;
  }
  .front-tagline {
    position: absolute; left: 1100px; top: 730px;
    font-size: 21px; color: var(--ink); white-space: nowrap;
  }
</style>
</head>
<body>
<main class="cover">
  <div class="cover-photo" role="img" aria-label="Soft grey textured stone background with a blurred warm horizontal light streak"></div>
  <div class="back-haze"></div>

  <div class="button-photo button-front" role="img" aria-label="Translucent silver shirt button"></div>
  <div class="button-photo button-back" role="img" aria-label="Translucent silver button seen at an angle"></div>

  <section class="blurb">
    <div class="blurb-label">Blurb</div>
    <p>A man lies dying and trapped in a parking garage stairwell. The poorly lit stairwell serves as a painful reminder of one of his memories of childhood locked in that darkened closet.</p>
    <p>To keep himself in tact he would play with a shiny silver button he ripped off from his pajamas – throwing it in the air and tapping the floor to find it. As he lies trapped and dying that same defeated and abandoned feeling descends upon him.</p>
    <p>As he comes in and out of consciousness memories from his past manifest themselves and we are introduced to the turbulent and sometimes triumphant pathway that has led him to his current state. It is up to him to sort through the barrage of emotions to find his way out, to let go, to forgive. That is if his heart will let him.</p>
  </section>

  <div class="isbn-area" aria-label="ISBN area"></div>

  <div class="spine-author">r.l. marsh</div>
  <div class="spine-title">the lantern</div>

  <div class="front-author">r.l. marsh</div>
  <h1 class="front-title">the lantern</h1>
  <div class="front-tagline">a novel</div>
</main>
</body>
</html>
```